Programme in the style of a 1920s (vintage) newspaper.

Format: 8-page brochure, stapled. A4 SIZE.

Bleed: 1mm all-around. Leave an additional 7mm clearance on left- and right-hand margins (see document attacked)

Style: Brochure will look like a newspaper from the 1920s. Old fonts should be used and an effect should be applied to all of the photos to make them appear older.

The brief: Attached is a .docx file which provides all of the content for this project. The photos will be uploaded within 7 days (we are taking them this week). But you can start this project without the photos as we have clearly indicated how many photos there will be and where (roughly) they should be positioned. You can choose what size you feel is right for each photo and leave that space blank for now.

```html
<!DOCTYPE html>
<html lang="en">
<head>
<meta charset="utf-8">
<title>The Circus Times – Special Edition</title>
<link rel="stylesheet" href="https://fonts.googleapis.com/css2?family=Ultra&family=Poiret+One&family=EB+Garamond:wght@400;500;600&display=swap">
<style>
  :root {
    --paper: #e9e7e1;
    --paper-edge: #dedbd3;
    --ink: #1c1b19;
    --ink-soft: #3a3935;
    --rule: #1e1d1b;
    --ad-light: #d9d6cf;
    --ad-dark: #8f8c86;
  }
  * { margin: 0; padding: 0; box-sizing: border-box; }
  html, body { width: 849px; height: 1200px; overflow: hidden; }
  body {
    background: radial-gradient(ellipse at center, var(--paper) 60%, var(--paper-edge) 100%);
    color: var(--ink);
    font-family: "EB Garamond", Georgia, serif;
    position: relative;
  }
  .masthead {
    position: absolute; top: 26px; left: 0; width: 849px;
    text-align: center;
    font-family: "Ultra", "Rockwell", serif;
    font-size: 47px; letter-spacing: 1px; line-height: 1;
  }
  .edition-bar {
    position: absolute; top: 108px; left: -2px; width: 853px; height: 45px;
    border: 2px solid var(--rule);
    font-family: "Poiret One", sans-serif;
    font-size: 17px; color: var(--ink-soft);
  }
  .edition-bar span { position: absolute; top: 11px; }
  .edition-name { left: 62px; }
  .edition-date { right: 45px; }
  .headline {
    position: absolute; left: 55px;
    font-weight: 600; line-height: 1;
  }
  .headline--lead { top: 207px; font-size: 33px; }
  .headline--second { top: 860px; font-size: 47px; font-weight: 400; }
  .column {
    position: absolute; width: 237px;
    font-size: 15.6px; line-height: 19.6px;
    text-align: justify; text-align-last: left;
  }
  .column p + p { margin-top: 19.6px; }
  .column .last { text-align-last: justify; }
  .ad {
    position: absolute;
    border: 1.5px solid var(--rule);
    background: linear-gradient(160deg, var(--ad-light), #c9c6bf);
  }
  .ad--voyage { background: linear-gradient(160deg, #d2cfc8, var(--ad-dark)); }
  .folio { position: absolute; left: 752px; top: 1154px; font-size: 16px; }
</style>
</head>
<body>
  <header>
    <h1 class="masthead">The Circus Times</h1>
    <div class="edition-bar">
      <span class="edition-name">Chaplin’s Circus Special Edition</span>
      <span class="edition-date">23rd August 1921</span>
    </div>
  </header>

  <article>
    <h2 class="headline headline--lead">Can Chaplin’s Circus save itself from bankruptcy?</h2>

    <div class="ad" style="left:55px;top:266px;width:236px;height:185px" role="img" aria-label="Vintage advertisement for a furniture and hardware store"></div>
    <div class="ad" style="left:307px;top:266px;width:236px;height:185px" role="img" aria-label="Vintage advertisement for a children's thumb guard"></div>

    <div class="column" style="left:55px;top:464px">
      <p>They say that drastic times call for drastic measures. Well, measures don’t come more drastic than this: Chaplin’s Circus has commissioned aviator Orval Whitmore—of ‘Whitmore Brothers’ fame—to build the world’s first Human Cannon!</p>
      <p>Chaplin’s Circus recently decided to sell its animals to rival circus-owner, Mr Barrington Brie, after a season of steadily declining ticket sales. This included their one-time star attraction Bambini the Elephant, whose popularity had been waning with public.</p>
    </div>

    <div class="column" style="left:307px;top:464px">
      <p>When questioned about the recent sale, Mr. Bottle, head of the Circus Owners Association, commented, “The sale of Chaplin’s animals confirms suspicions amongst the circus community that this small-time family circus is on its way out. The public want to see animals! Chaplin’s Circus is out of touch!”</p>
      <p class="last">Chaplin’s Ringmaster, Mark Mergana, had the following to say: “We took a group decision to become the world’s first all-human circus. People don’t want to see animals doing tricks any more, they want danger and excitement. If you</p>
    </div>

    <div class="column" style="left:558px;top:258px">
      <p>thought the Charleston was fast, just wait until you see our human cannonball flying across the Big Top! Do not blink or you’ll miss him! This is going to be the most spectacular circus show on Earth!”</p>
      <p>The spectacle does not stop there, Ladies and Gentlemen. Oh, no! Various sources have confirmed that world-famous trapeze artist Pansy Zedora has been recruited in an attempt to get this show back on top. [Insert photo #3] Ms Zedora first made a name for herself as The Human Arrow with the Flying Zedoras. Although she no longer performs as frequently as she once did, Chaplin’s Circus hopes her world-renowned reputation will pack out the Big Top, once more.</p>
      <p class="last">So the question remains: Will Chaplin’s Circus’ new strategy pay off? Will they be able to save themselves from the perils of bankruptcy? Well, if acts like these cannot keep this circus alive, nothing can!</p>
    </div>
  </article>

  <article>
    <h2 class="headline headline--second">The vultures are circling.</h2>

    <div class="ad ad--voyage" style="left:55px;top:928px;width:238px;height:182px" role="img" aria-label="Vintage steamship voyage advertisement with a map"></div>

    <div class="column" style="left:307px;top:926px">
      <p class="last">An inside source has revealed that circus owners from across the country are already making arrangements to mount a hostile takeover of Chaplin’s Circus. Spearheading this campaign is Barrington Brie, the fourth-generation owner of England’s largest circus, Cirque du Brie, who hopes to turn Chaplin’s Circus’ Big Top into a touring reptile exhibition!</p>
    </div>

    <div class="column" style="left:558px;top:868px">
      <p>Mr Brie does not keep his hatred for Chaplin’s Circus a secret: “Over the past few years, I have made a number of generous offers to buy Chaplin’s Circus. When they fail, and they will, my offer will not be so generous. Let this be a lesson to the circus industry… I always get what I want.”</p>
      <p class="last">Let’s hope, for the sake of Chaplin’s Circus, that their two newly acquired acts can keep the dogs at bay.</p>
    </div>
  </article>

  <footer class="folio">Page 1</footer>
</body>
</html>
```